Flyer-Design für Werbeflyer Teamentwicklung/Coaching als pdf
Zielgruppe
ich berate Personen, Teams und Organisationseinheiten, überwiegend im Profitbereich. (Internationale Konzerne). Mein Beratungsspektrum ist Führung, Prozessverbesserungen, Teamentwicklung
Aufgabenstellung
Der Text ist in Anlehnung an meine HP, Teamentwicklung und Coaching und es sollte eine übersichtliche, infomative 1-2 Seiten entstehen, die ich als erste Werbung/Kontaktaufnahme versenden kann. Die Seiten sollen klar einen Überblick über mein "Schaffen" geben, sollen aber auch schon etwas von meiner Arbeitsweise deutlich machen. (Ich begriefe schnell, formuliere klar und arbeite sehr zielorientiert - allerdings auch schnörkellos!) Diese Seiten sollten überwiegend als Anhang an eine Mail fungieren, im Ausnahmefall aber auch versendet werden.
Das Logo, die Farbe, etc. analog zu meiner HP - ich lass mich da aber auch gern beraten, falls sie andere Ideen haben

```html
<!DOCTYPE html>
<html lang="de">
<head>
<meta charset="utf-8">
<title>Teamentwicklung – Brigitte Morell</title>
<link href="https://fonts.googleapis.com/css2?family=Open+Sans:wght@400;600&family=Tinos:wght@700&display=swap" rel="stylesheet">
<style>
  :root {
    --band: #b9c6c3;
    --plum: #7a0a50;
    --slate: #646d6c;
    --text: #5f6766;
    --paper: #ffffff;
    --logo-grey: #9aa5a4;
    --photo-tone: #a3c7c3;
  }
  * { margin: 0; padding: 0; box-sizing: border-box; }
  html, body { width: 1200px; height: 848px; overflow: hidden; background: var(--paper); }
  .flyer {
    position: relative; width: 1200px; height: 848px; overflow: hidden;
    background: var(--paper);
    font-family: "Open Sans", Arial, sans-serif; color: var(--text);
  }
  .hero-photo {
    position: absolute; left: 0; top: 0; width: 586px; height: 848px;
    background: var(--photo-tone);
  }
  .accent-block {
    position: absolute; left: 1089px; top: 0; width: 77px; height: 163px;
    background: var(--plum);
  }
  .header-band {
    position: absolute; left: 0; top: 21px; width: 1200px; height: 82px;
    background: var(--band);
  }
  .brand-mark {
    position: absolute; left: 51px; top: 21px; width: 86px; height: 82px;
    background: var(--logo-grey);
    display: flex; align-items: center; justify-content: center; text-align: center;
    color: var(--paper); font-weight: 600; font-size: 12px; line-height: 1.25;
  }
  .motto-frame { position: absolute; left: 778px; top: 27px; width: 330px; height: 70px; }
  .motto {
    position: absolute; left: 778px; top: 27px; width: 350px; height: 70px;
    font-family: "Tinos", "Times New Roman", serif; font-weight: 700;
    color: var(--paper); font-size: 17px; line-height: 1;
  }
  .motto span { position: absolute; white-space: nowrap; }
  .motto .line-1 { left: 22px; top: 12px; }
  .motto .line-2 { left: 74px; top: 38px; }
  .motto .quote-open { left: -2px; top: 6px; font-size: 28px; }
  .motto .quote-close { left: 325px; top: 40px; font-size: 28px; }
  .headline {
    position: absolute; left: 600px; top: 272px; width: 474px; text-align: right;
    font-weight: 600; color: var(--slate); font-size: 41.5px; line-height: 38px; letter-spacing: 0.3px;
  }
  .headline .surname { color: var(--plum); }
  .intro, .list-lead, .services {
    position: absolute; left: 744px; width: 440px;
    font-size: 15px; line-height: 17.9px; white-space: nowrap;
  }
  .intro { top: 377px; }
  .list-lead { top: 516px; }
  .services { top: 549px; list-style: none; }
  .services li { position: relative; padding-left: 19px; margin-bottom: 18px; }
  .services li::before {
    content: ""; position: absolute; left: 0; top: 5px; width: 8px; height: 8px;
    background: var(--plum);
  }
  .contact-card {
    position: absolute; left: 53px; top: 538px; width: 267px; height: 253px;
    background: rgba(255,255,255,0.72);
    border: 3px solid rgba(255,255,255,0.55);
    padding: 11px 0 0 53px;
    font-size: 15px; line-height: 17.9px; color: var(--text); white-space: nowrap;
  }
  .contact-card h2 { font-weight: 600; font-size: 30px; line-height: 36px; color: var(--slate); letter-spacing: 0.3px; }
  .contact-card .contact-name { color: var(--plum); margin: 10px 0 18px; }
  .contact-card .address { margin-bottom: 17px; }
</style>
</head>
<body>
<main class="flyer">
  <div class="hero-photo" role="img" aria-label="Foto: Holzsteg mit weißem Geländer, der aufs Meer hinausführt"></div>

  <div class="accent-block"></div>
  <div class="header-band"></div>
  <div class="brand-mark">Brigitte<br>Morell</div>

  <svg class="motto-frame" width="330" height="70" viewBox="0 0 330 70" aria-hidden="true">
    <g fill="none" stroke="#ffffff" stroke-width="3">
      <path d="M44 1.5 H1.5 V68.5 H44"/>
      <path d="M286 1.5 H328.5 V68.5 H286"/>
    </g>
  </svg>
  <p class="motto">
    <span class="quote-open">“</span>
    <span class="line-1">Zu erkennen was geschieht,</span>
    <span class="line-2">ist der Beginn der Veränderung.</span>
    <span class="quote-close">„</span>
  </p>

  <h1 class="headline">TEAMENTWICKLUNG<br>BRIGITTE <span class="surname">MORELL</span></h1>

  <p class="intro">Teams sind lebendige Gebilde, die um erfolgreich zu sein,<br>sich immer wieder neu ausrichten und koordinieren müs-<br>sen. Das tun sie in aller Regel ohne fremde Hilfe - aber ab<br>und zu ist es hilfreich, Impulse oder Entwicklungsförde-<br>rung von außen bekommen.</p>

  <p class="list-lead">Dazu gehören</p>

  <ul class="services">
    <li>Eine sorgfältige Analyse der Situation und Festlegung<br>gewünschter Resultate</li>
    <li>Überzeugende und förderliche Methoden, die die<br>Lösungskompetenzen der Menschen im Team unter<br>stützen</li>
    <li>Klare Führung durch den Widerstreit von Teaminteres-<br>sen zwischen Verändern, Bewahren, Harmonie und<br>Konfliktbearbeitung, klarem Feed back und Eintracht<br>im Team</li>
    <li>Tragfähigkeit der Ergebnisse</li>
  </ul>

  <section class="contact-card">
    <h2>KONTAKT</h2>
    <p class="contact-name">Brigitte Morell</p>
    <p class="address">Lindenhof<br>Lindenstraße 14-16<br>90402 Nürnberg</p>
    <p class="channels">Tel:&nbsp; 0911 - 55 01 23<br>Fax: 0911 - 5 50 12 49<br>info@brigitte-morell.de<br>www.brigitte-morell.de</p>
  </section>
</main>
</body>
</html>
```